K & D A/C Compressors' Business Card

Hello,

I need someone to create a new business card for my business. The name of my Business is: K & D A/C Compressors. I sell automotive air conditioning parts (a/c parts). I would like the business card to incorporate my logo, and to have an automotive feel to it. It is important that the business card feel like it is coming from an automotive parts business.

I already have a logo, which I will provide.

Thanks.

Project Deadline Extended Reason: I feel like extending the deadline until October 9, 2017, will allow for more time to design the business card. Thank you for your understanding. Added Monday, October 2, 2017

Target Market(s)

Consumers who need automotive a/c parts, and auto mechanics.

Industry/Entity Type

Automotive

Contact Information for Business Card

Business name: K & D A/C Compressors
Business Address: 48207 Southwest 64th Avenue, North Miami Beach, Florida 33847
Telephone: 305-642-1730
Fax: To be provided once I choose your design.
Website: www.kdcoolparts.example
Email: support@kdcoolparts.example
Names: To be provided once I choose your design.

Font styles to use
Sans Serif

Colors

Designer to choose colors to be used in the design.

Requirements
Must have
• The business card must include all of the "Business Card Details" and the logo I have uploaded.

```html
<!DOCTYPE html>
<html lang="en">
<head>
<meta charset="utf-8">
<title>K &amp; D A/C Compressors – Business Card</title>
<link href="https://fonts.googleapis.com/css2?family=Arimo:wght@400;700&display=swap" rel="stylesheet">
<style>
  :root {
    --backdrop: #2b2d2d;
    --card: #231f20;
    --brand-grey: #a7a9ac;
    --accent-blue: #1aa7e0;
    --text-light: #f2f2f2;
    --text-muted: #bdbdbd;
    --divider: #4a4647;
  }
  html, body {
    margin: 0;
    width: 1200px;
    height: 1200px;
    overflow: hidden;
    background: var(--backdrop);
    font-family: "Arimo", Arial, sans-serif;
  }
  .card {
    position: absolute;
    left: 150px;
    width: 900px;
    height: 514px;
    background: var(--card);
    border-radius: 34px;
    box-shadow: 0 10px 30px rgba(0,0,0,.45);
  }
  .card--logo { top: 56px; }
  .card--details { top: 630px; }

  .wordmark {
    display: flex;
    align-items: center;
    gap: 18px;
    color: var(--brand-grey);
    font-weight: 700;
    line-height: 1.05;
  }
  .wordmark__dot {
    flex: none;
    border-radius: 50%;
    background: var(--brand-grey);
  }
  .card--logo .wordmark {
    position: absolute;
    left: 0; right: 0; top: 0; bottom: 0;
    justify-content: center;
    font-size: 58px;
  }
  .card--logo .wordmark__dot { width: 40px; height: 40px; }

  .card--details .wordmark {
    position: absolute;
    left: 60px;
    top: 120px;
    width: 320px;
    font-size: 40px;
    flex-wrap: nowrap;
  }
  .card--details .wordmark__dot { width: 28px; height: 28px; }

  .divider {
    position: absolute;
    left: 410px;
    top: 70px;
    width: 1px;
    height: 374px;
    background: var(--divider);
  }
  .contact {
    position: absolute;
    left: 450px;
    top: 80px;
    right: 40px;
    color: var(--text-light);
  }
  .contact__name {
    margin: 0;
    color: var(--accent-blue);
    font-size: 34px;
    font-weight: 700;
    letter-spacing: -.5px;
    text-transform: uppercase;
  }
  .contact__title {
    margin: 4px 0 26px;
    color: var(--text-muted);
    font-size: 22px;
  }
  .contact__address {
    margin: 0 0 26px;
    font-size: 22px;
    font-style: normal;
    line-height: 1.3;
  }
  .contact__list {
    list-style: none;
    margin: 0;
    padding: 0;
    font-size: 22px;
  }
  .contact__list li {
    display: flex;
    align-items: center;
    gap: 12px;
    margin-bottom: 8px;
  }
  .contact__list svg {
    width: 20px;
    height: 20px;
    flex: none;
    fill: var(--accent-blue);
  }
</style>
</head>
<body>

<section class="card card--logo">
  <div class="wordmark">
    <span class="wordmark__dot"></span>
    <span>K &amp; D A/C Compressors</span>
  </div>
</section>

<section class="card card--details">
  <div class="wordmark">
    <span class="wordmark__dot"></span>
    <span>K &amp; D<br>A/C Compressors</span>
  </div>

  <div class="divider"></div>

  <div class="contact">
    <h1 class="contact__name">Marcus Delgado</h1>
    <p class="contact__title">Managing Director</p>
    <address class="contact__address">
      48207 Southwest 64th Avenue<br>
      North Miami Beach
    </address>
    <ul class="contact__list">
      <li>
        <svg viewBox="0 0 24 24" aria-hidden="true"><path d="M6.6 10.8a15 15 0 0 0 6.6 6.6l2.2-2.2c.3-.3.7-.4 1-.2 1.1.4 2.3.6 3.6.6.6 0 1 .4 1 1V20c0 .6-.4 1-1 1A17 17 0 0 1 3 4c0-.6.4-1 1-1h3.5c.6 0 1 .4 1 1 0 1.3.2 2.5.6 3.6.1.3 0 .7-.2 1z"/></svg>
        305-642-1730
      </li>
      <li>
        <svg viewBox="0 0 24 24" aria-hidden="true"><path d="M7 3h8l3 3v4H7zM4 10h16a1 1 0 0 1 1 1v8a1 1 0 0 1-1 1H4a1 1 0 0 1-1-1v-8a1 1 0 0 1 1-1zm3 3v2h6v-2z"/></svg>
        305-642-1735
      </li>
      <li>
        <svg viewBox="0 0 24 24" aria-hidden="true"><path d="M3 5h18v14H3zm2 2v.5l7 5 7-5V7l-7 5z"/></svg>
        support@kdcoolparts.example
      </li>
      <li>
        <svg viewBox="0 0 24 24" aria-hidden="true"><path d="M12 2a10 10 0 1 0 0 20 10 10 0 0 0 0-20zm-1 17.9A8 8 0 0 1 4.1 11H7c.1 3.3 1.6 6.3 4 8.9zm0-10.9H9c.2-2.4 1.1-4.7 2-6.5zm2 0V2.5c.9 1.8 1.8 4.1 2 6.5zm0 2h2c-.2 2.6-1 5.2-2 7.2zm-2 0v7.2c-1-2-1.8-4.6-2-7.2zm6 0h2.9a8 8 0 0 1-6.9 6.9c1.6-2 3.3-4.4 4-6.9zm0-2c-.2-2.4-1.1-4.9-2.5-6.7A8 8 0 0 1 19.9 9z"/></svg>
        www.kdcoolparts.example
      </li>
    </ul>
  </div>
</section>

</body>
</html>
```